Brick nest business card for client

Require a business card design for a new company based in Trinidad & Tobago called "Brick nest".

We source building supplies for resident and commercial projects. We manage and supply all your building solutions.

Exp: If you was to build a house or commercial building, My company Brick nest will supply and install all your building needs. Floor tile, Windows, Door, Molding .

Target Market(s)

Construction client

Industry/Entity Type

Building

Contact Information for Business Card

BRICK NEST LIMITED
VERDANT TRADE COURT
LA PALMERA, EXT. NO. 4, BLDG 3
SAN JUAN, TRINIDAD, W.I.
868-642-9087
bricknestlimited.example
derek@bricknestlimited.example

Font styles to use
Serif

Requirements
Must have
• Company name
• Address
• My Name: Derek Rampersook
• Director
Nice to have
• Modern business card (With a new logo)

```html
<!DOCTYPE html>
<html lang="en">
<head>
<meta charset="utf-8">
<title>Brick Nest Limited – Business Card</title>
<link rel="stylesheet" href="https://fonts.googleapis.com/css2?family=Noto+Serif:wght@400;700&display=swap">
<style>
  :root {
    --backdrop: #e9e9ec;
    --card: #ffffff;
    --ink: #1a1a1a;
    --watermark: #e3f0f7;
    --tab-grey: #aab2b9;
    --tab-light: #c9cfd4;
    --icon: #1a1a1a;
    --accent: #d8a75a;
  }
  * { box-sizing: border-box; margin: 0; padding: 0; }
  html, body {
    width: 1200px; height: 800px; overflow: hidden;
    background: var(--backdrop);
    font-family: "Noto Serif", Georgia, serif;
    color: var(--ink);
  }
  .card {
    position: absolute; left: 180px; top: 160px;
    width: 840px; height: 480px;
    background: var(--card);
    overflow: hidden;
    box-shadow: 0 10px 30px rgba(0,0,0,.15);
  }
  .corner-tabs { position: absolute; left: 0; top: 0; }
  .watermark {
    position: absolute; left: 110px; top: 120px;
    font-size: 140px; line-height: 1;
    color: var(--watermark);
    white-space: nowrap;
  }
  .contact {
    position: absolute; left: 60px; top: 160px;
    font-size: 18px; line-height: 30px;
  }
  .contact .row { display: flex; align-items: center; gap: 10px; }
  .contact svg { width: 18px; height: 18px; flex: none; }
  .brand {
    position: absolute; right: 40px; top: 150px;
    width: 320px; text-align: right;
  }
  .brand-name {
    display: flex; align-items: center; justify-content: flex-end; gap: 14px;
    font-size: 44px; line-height: 1; white-space: nowrap;
  }
  .brand-mark { width: 26px; height: 26px; background: var(--accent); flex: none; }
  .brand-limited { font-size: 18px; letter-spacing: 8px; margin-top: 8px; }
  .brand-tagline { font-size: 14px; margin-top: 4px; }
  .person {
    position: absolute; right: 40px; top: 330px;
    text-align: right;
  }
  .person-name { font-size: 24px; font-weight: 700; line-height: 1.3; }
  .person-title { font-size: 16px; letter-spacing: 3px; color: #555; }
</style>
</head>
<body>
  <main class="card">
    <svg class="corner-tabs" width="260" height="70" viewBox="0 0 260 70" aria-hidden="true">
      <path d="M0 0 H250 L230 30 H60 Q40 30 30 50 L20 70 H0 Z" fill="var(--tab-light)"/>
      <path d="M0 0 H200 L185 20 H45 Q30 20 22 38 L14 60 H0 Z" fill="var(--tab-grey)"/>
    </svg>

    <div class="watermark" aria-hidden="true">Brick nest</div>

    <section class="contact">
      <p>Verdant Trade Court la palmera,</p>
      <p>EXT.NO.4, bldg 3 san juan, Trinidad, W.I.</p>
      <p class="row">
        <svg viewBox="0 0 18 18"><rect width="18" height="18" rx="3" fill="var(--icon)"/><path d="M5 4 L7 4 L8 7 L6.5 8 Q8 11 10 11.5 L11 10 L14 11 L14 13 Q9 15 5 9 Q4 6 5 4 Z" fill="#fff"/></svg>
        868-642-9087
      </p>
      <p class="row">
        <svg viewBox="0 0 18 18"><rect width="18" height="18" rx="3" fill="var(--icon)"/><circle cx="9" cy="9" r="5" fill="none" stroke="#fff" stroke-width="1.4"/><path d="M4 9 H14 M9 4 Q6 9 9 14 M9 4 Q12 9 9 14" fill="none" stroke="#fff" stroke-width="1.1"/></svg>
        www.bricknestlimited.example
      </p>
      <p class="row">
        <svg viewBox="0 0 18 18"><rect width="18" height="18" rx="3" fill="var(--icon)"/><rect x="4" y="5.5" width="10" height="7" fill="none" stroke="#fff" stroke-width="1.3"/><path d="M4 5.5 L9 10 L14 5.5" fill="none" stroke="#fff" stroke-width="1.3"/></svg>
        derek@bricknestlimited.example
      </p>
    </section>

    <section class="brand">
      <div class="brand-name"><span class="brand-mark"></span>Brick Nest</div>
      <div class="brand-limited">LIMITED</div>
      <div class="brand-tagline">For All Your Building Solutions</div>
    </section>

    <section class="person">
      <p class="person-name">Derek Rampersook</p>
      <p class="person-title">DIRECTOR</p>
    </section>
  </main>
</body>
</html>
```